Business Card Design Project

We need a business card design for an existing company in Dallas/Fort Worth that is expanding services and re-branding. We are changing the name from Brightmoor Commercial Cleaning to Keystride Facility Services. We are expanding from only commercial cleaning to include complete commercial landscape and facility maintenance services, too.

As stated, we offer a package of services that includes landscape, janitorial and facility services, which is largely unique in the industry.

We would like a design that communicates trust/partnership with a professional, corporate image, but not necessarily using the standard white business card. We would like a design that perhaps uses darker blues or perhaps a gray background, but we are open to other ideas. We might also be interested in a double-sided design - maybe with our logo on the back, printed on a gray background?

We will probably stick with the attached logo, but if you've got another inspired idea....

Target Market(s)

Property managers, commercial real estate professionals, corporate executives

Industry/Entity Type

Landscape

Requirements
Should not have
• Not interested in old style fonts.

```html
<!DOCTYPE html>
<html lang="en">
<head>
<meta charset="utf-8">
<title>Keystride Facility Services – Business Card</title>
<link rel="stylesheet" href="https://fonts.googleapis.com/css2?family=Questrial&family=League+Spartan:wght@700&display=swap">
<style>
  :root {
    --backdrop: #3b3b3d;
    --charcoal: #2a2a2b;
    --charcoal-strip: #2c2c2d;
    --blue-light: #1ba8e6;
    --blue-mid: #1290d6;
    --blue-deep: #0a6fc0;
    --ink-dark: #2b2b2d;
    --white: #ffffff;
  }
  * { margin: 0; padding: 0; box-sizing: border-box; }
  html, body { width: 1200px; height: 900px; overflow: hidden; }
  body { background: var(--backdrop); position: relative; }

  .card {
    position: absolute; left: 73px; top: 135px;
    width: 1052px; height: 600px;
    background: var(--charcoal);
    overflow: hidden;
  }

  .brand-band { position: absolute; left: 0; top: 0; width: 100%; height: 213px; background: var(--charcoal); }
  .brand-name {
    position: absolute; left: 0; top: 62px; width: 100%;
    text-align: center;
    font-family: "League Spartan", sans-serif; font-weight: 700;
    font-size: 50px; letter-spacing: 4px; line-height: 1;
    color: var(--white); text-transform: uppercase; white-space: nowrap;
  }
  .tagline {
    position: absolute; left: 0; top: 150px; width: 100%;
    text-align: center;
    font-family: "Questrial", sans-serif; font-style: italic;
    font-size: 25px; color: var(--white); white-space: nowrap;
  }

  .contact-panel {
    position: absolute; left: 0; top: 213px; width: 100%; height: 387px;
    background: radial-gradient(ellipse at 50% 30%, var(--blue-light) 0%, var(--blue-mid) 55%, var(--blue-deep) 100%);
  }
  .contact-line {
    position: absolute; left: 0; width: 100%; text-align: center;
    font-family: "League Spartan", sans-serif; font-weight: 700;
    color: var(--ink-dark); text-transform: uppercase; letter-spacing: 4px;
    font-size: 34px; line-height: 1; white-space: nowrap;
  }
  .person { top: 56px; letter-spacing: 5px; }
  .email { top: 140px; }
  .website { top: 184px; }

  .details-strip {
    position: absolute; left: 0; top: 256px; width: 100%; height: 68px;
    background: var(--charcoal-strip);
  }
  .detail {
    position: absolute; font-family: "League Spartan", sans-serif; font-weight: 700;
    color: var(--white); font-size: 25px; letter-spacing: 2px; line-height: 30px;
    text-transform: uppercase; white-space: nowrap;
  }
  .detail-icon { position: absolute; }
  .address { left: 126px; top: 4px; }
  .phone { left: 467px; top: 20px; }
  .fax { left: 803px; top: 20px; }
</style>
</head>
<body>
  <div class="card">
    <header class="brand-band">
      <p class="brand-name">Keystride Facility Services</p>
      <p class="tagline">One Source For Landscape, Janitorial and Facility Maintenance</p>
    </header>

    <section class="contact-panel">
      <p class="contact-line person">Dale Whitford &nbsp;|&nbsp; General Manager</p>
      <p class="contact-line email">dale@keystridefacilityservices.com</p>
      <p class="contact-line website">www.keystridefacilityservices.com</p>

      <div class="details-strip">
        <svg class="detail-icon" style="left:69px;top:22px" width="32" height="24" viewBox="0 0 32 24">
          <rect x="0" y="0" width="32" height="24" rx="3" fill="#fff"/>
          <path d="M1 2 L16 14 L31 2" fill="none" stroke="#2c2c2d" stroke-width="2"/>
        </svg>
        <p class="detail address">123 Main St.<br>City, State Zip</p>

        <svg class="detail-icon" style="left:421px;top:18px" width="22" height="32" viewBox="0 0 22 32">
          <rect x="0" y="0" width="22" height="32" rx="4" fill="#fff"/>
          <rect x="3" y="4" width="16" height="20" fill="#2c2c2d"/>
          <circle cx="11" cy="28" r="2" fill="#2c2c2d"/>
        </svg>
        <p class="detail phone">000.000.0000</p>

        <svg class="detail-icon" style="left:745px;top:17px" width="34" height="34" viewBox="0 0 34 34">
          <rect x="8" y="0" width="18" height="10" fill="#fff"/>
          <rect x="0" y="10" width="34" height="16" rx="3" fill="#fff"/>
          <rect x="7" y="18" width="20" height="16" fill="#fff" stroke="#2c2c2d" stroke-width="2"/>
          <line x1="11" y1="23" x2="23" y2="23" stroke="#2c2c2d" stroke-width="2"/>
          <line x1="11" y1="28" x2="23" y2="28" stroke="#2c2c2d" stroke-width="2"/>
        </svg>
        <p class="detail fax">000.000.0000</p>
      </div>
    </section>
  </div>
</body>
</html>
```